BrovaLT BIZ Card, email signature & Stationary

Professional business cards, email signatures and ms word letterhead

Target Market(s)

business owners

Industry/Entity Type

cloud hosting

Contact Information for Business Card

name title office phone number , direct line, fax email address web site

Font styles to use
Other font styles liked:
• something that compliments font in logo

```html
<!DOCTYPE html>
<html lang="en">
<head>
<meta charset="utf-8">
<title>BrovaLT Stationery</title>
<link rel="stylesheet" href="https://fonts.googleapis.com/css2?family=Montserrat:wght@400;500&display=swap">
<style>
  :root{
    --bg:#d1d1d5;
    --paper:#ffffff;
    --red:#e31b23;
    --red-dark:#a8141a;
    --black:#000000;
    --navy:#0f1a2b;
    --ink:#1b1b1b;
    --window:#dcdcdc;
  }
  *{margin:0;padding:0;box-sizing:border-box}
  html,body{width:1200px;height:1017px;overflow:hidden}
  body{background:var(--bg);font-family:"Montserrat",sans-serif;color:var(--ink);position:relative}
  .item{position:absolute;background:var(--paper);overflow:hidden}
  .band{position:absolute;left:0;display:block}
  .wordmark{position:absolute;color:var(--red);font-weight:400;letter-spacing:-0.5px;line-height:1;white-space:nowrap}
  .centered{left:0;right:0;text-align:center}
  .web{position:absolute;color:#fff;font-size:8px;letter-spacing:1px;white-space:nowrap}

  .contact-strip{position:absolute;display:flex;gap:9px;font-size:5px;white-space:nowrap;align-items:center}
  .contact-strip span{display:flex;align-items:center;gap:3px}
  .mini-icon{width:6px;height:6px;border:0.6px solid var(--red);border-radius:1px;display:inline-block}
  .contact-strip.on-dark{color:#fff}
  .contact-strip.on-dark .mini-icon{border-color:#fff}

  /* letterhead */
  .letterhead{left:80px;top:48px;width:317px;height:448px}
  .letterhead .wordmark{right:42px;top:27px;font-size:28px}

  /* business card front */
  .card-front{left:445px;top:89px;width:277px;height:159px}
  .card-front .wordmark{left:13px;top:60px;font-size:26px}
  .person{position:absolute;left:140px;top:20px}
  .person .name{font-size:13px;font-weight:400;color:var(--ink);line-height:1}
  .person .role{font-size:7px;margin-top:3px;letter-spacing:.3px}
  .contact-list{position:absolute;left:140px;top:54px;list-style:none}
  .contact-list li{display:flex;align-items:center;gap:5px;font-size:7.6px;height:18px;letter-spacing:.2px}
  .contact-list svg{width:11px;height:11px;flex:none}

  /* business card back */
  .card-back{left:445px;top:298px;width:277px;height:158px}
  .card-back .wordmark{top:42px;font-size:27px}
  .card-back .web{right:20px;top:129px}

  /* notebook */
  .notebook{left:771px;top:48px;width:317px;height:448px}
  .notebook .wordmark{top:72px;font-size:28px}
  .notebook .web{left:0;right:0;text-align:center;top:411px;letter-spacing:2px;font-size:8.5px}

  /* folder */
  .folder-flaps{position:absolute;left:81px;top:536px}
  .folder-inside{left:156px;top:536px;width:283px;height:365px;background:var(--black)}
  .folder-inside .contact-strip{left:9px;top:348px}
  .folder-cover{left:439px;top:536px;width:284px;height:365px}
  .folder-cover .wordmark{top:130px;font-size:28px}
  .folder-cover .web{right:26px;top:325px;letter-spacing:1.3px}

  /* envelope front */
  .envelope-front{left:779px;top:535px;width:372px;height:173px}
  .envelope-front .wordmark{left:28px;top:64px;font-size:27px}
  .envelope-window{position:absolute;left:220px;top:58px;width:110px;height:44px;border-radius:4px;background:linear-gradient(160deg,#e9e9e9,var(--window) 55%,#ececec);border:1px solid #c6c6c6}
  .envelope-front .web{right:16px;top:155px}

  /* envelope back */
  .envelope-back{left:779px;top:737px;width:372px;height:174px;border:1px solid #c9c9c9}
  .envelope-back .flap{position:absolute;left:0;top:0}
  .envelope-back .wordmark{top:25px;font-size:15px}
</style>
</head>
<body>

<!-- Letterhead -->
<section class="item letterhead" aria-label="Letterhead">
  <div class="wordmark">BrovaLT</div>
  <div class="contact-strip" style="left:36px;top:405px">
    <span><i class="mini-icon"></i>0000 0000 0000</span>
    <span><i class="mini-icon"></i>Your email address here</span>
    <span><i class="mini-icon"></i>Your web address here</span>
    <span><i class="mini-icon"></i>Your Address Here</span>
  </div>
  <svg class="band" style="top:407px" width="317" height="41" viewBox="0 0 317 41">
    <polygon points="0,0 48,13 0,30" fill="var(--red)"/>
    <rect x="48" y="12" width="269" height="2.5" fill="var(--navy)"/>
    <polygon points="48,13 51,14.5 0,33 0,30" fill="var(--navy)"/>
    <polygon points="54,20 317,20 317,41 0,41 0,38" fill="var(--black)"/>
  </svg>
</section>

<!-- Business card front -->
<section class="item card-front" aria-label="Business card front">
  <div class="wordmark">BrovaLT</div>
  <div class="person">
    <p class="name">Person Name</p>
    <p class="role">Chief Executive</p>
  </div>
  <ul class="contact-list">
    <li>
      <svg viewBox="0 0 12 12"><rect x=".5" y=".5" width="11" height="11" rx="1.5" fill="none" stroke="var(--red)"/><path d="M4 3.2l1.2 1.4-.6.8c.4.9 1.1 1.6 2 2l.8-.6 1.4 1.2-.8 1c-2.3-.3-4.1-2.1-4.4-4.4z" fill="var(--red)"/></svg>
      Phone: 000 0000 0000
    </li>
    <li>
      <svg viewBox="0 0 12 12"><rect x=".5" y=".5" width="11" height="11" rx="1.5" fill="none" stroke="var(--red)"/><rect x="2.8" y="3.8" width="6.4" height="4.4" fill="var(--red)"/><path d="M2.8 3.8L6 6.4l3.2-2.6" fill="none" stroke="#fff" stroke-width=".6"/></svg>
      Your email address here
    </li>
    <li>
      <svg viewBox="0 0 12 12"><rect x=".5" y=".5" width="11" height="11" rx="1.5" fill="none" stroke="var(--red)"/><circle cx="6" cy="6" r="3" fill="none" stroke="var(--red)" stroke-width=".7"/><path d="M3 6h6M6 3c-1.4 1.6-1.4 4.4 0 6M6 3c1.4 1.6 1.4 4.4 0 6" fill="none" stroke="var(--red)" stroke-width=".5"/></svg>
      Your web address here
    </li>
    <li>
      <svg viewBox="0 0 12 12"><rect x=".5" y=".5" width="11" height="11" rx="1.5" fill="none" stroke="var(--red)"/><path d="M6 9.5C4.2 7.4 3.5 6.2 3.5 5a2.5 2.5 0 015 0c0 1.2-.7 2.4-2.5 4.5z" fill="var(--red)"/><circle cx="6" cy="5" r=".9" fill="#fff"/></svg>
      Your Address Line Here
    </li>
  </ul>
  <svg class="band" style="top:123px" width="277" height="36" viewBox="0 0 277 36">
    <polygon points="0,0 44,12 0,27" fill="var(--red)"/>
    <rect x="44" y="11" width="233" height="2.3" fill="var(--navy)"/>
    <polygon points="44,12 47,13.3 0,30.5 0,28" fill="var(--navy)"/>
    <polygon points="50,19 277,19 277,36 0,36 0,35" fill="var(--black)"/>
  </svg>
</section>

<!-- Business card back -->
<section class="item card-back" aria-label="Business card back">
  <div class="wordmark centered">BrovaLT</div>
  <svg class="band" style="top:99px" width="277" height="59" viewBox="0 0 277 59">
    <polygon points="0,0 44,12 0,27" fill="var(--red)"/>
    <rect x="44" y="11" width="233" height="2.3" fill="var(--navy)"/>
    <polygon points="44,12 47,13.3 0,30.5 0,28" fill="var(--navy)"/>
    <polygon points="50,19 277,19 277,59 0,59 0,35" fill="var(--black)"/>
  </svg>
  <div class="web">www.brovalt-cloud.com</div>
</section>

<!-- Notebook cover -->
<section class="item notebook" aria-label="Notebook cover">
  <div class="wordmark centered">BrovaLT</div>
  <svg class="band" style="top:156px" width="317" height="292" viewBox="0 0 317 292">
    <polygon points="0,0 48,14 0,31" fill="var(--red)"/>
    <rect x="48" y="13" width="269" height="2.5" fill="var(--navy)"/>
    <polygon points="48,14 51,15.5 0,34 0,31" fill="var(--navy)"/>
    <polygon points="54,21 317,21 317,292 0,292 0,39" fill="var(--black)"/>
  </svg>
  <div class="web">www.brovalt-cloud.com</div>
</section>

<!-- Presentation folder -->
<svg class="folder-flaps" width="358" height="440" viewBox="0 0 358 440" aria-hidden="true">
  <defs>
    <linearGradient id="flapSide" x1="0" x2="1" y1="0" y2="0">
      <stop offset="0" stop-color="var(--red)"/>
      <stop offset="1" stop-color="var(--red-dark)"/>
    </linearGradient>
    <linearGradient id="flapBottom" x1="0" x2="0" y1="0" y2="1">
      <stop offset="0" stop-color="var(--red-dark)"/>
      <stop offset="1" stop-color="var(--red)"/>
    </linearGradient>
  </defs>
  <path d="M75 0 L14 16 Q0 20 0 34 L0 330 Q0 344 14 348 L75 365 Z" fill="url(#flapSide)"/>
  <path d="M75 365 L358 365 L335 428 Q331 440 318 440 L115 440 Q102 440 98 428 Z" fill="url(#flapBottom)"/>
</svg>
<section class="item folder-inside" aria-label="Folder inside panel">
  <div class="contact-strip on-dark">
    <span><i class="mini-icon"></i>0000 0000 0000</span>
    <span><i class="mini-icon"></i>Your email address here</span>
    <span><i class="mini-icon"></i>Your web address here</span>
    <span><i class="mini-icon"></i>Your Address Here</span>
  </div>
</section>
<section class="item folder-cover" aria-label="Folder cover">
  <div class="wordmark centered">BrovaLT</div>
  <svg class="band" style="top:281px" width="284" height="84" viewBox="0 0 284 84">
    <polygon points="0,0 44,13 0,29" fill="var(--red)"/>
    <rect x="44" y="12" width="240" height="2.5" fill="var(--navy)"/>
    <polygon points="44,13 47,14.5 0,32 0,29" fill="var(--navy)"/>
    <polygon points="50,20 284,20 284,84 0,84 0,37" fill="var(--black)"/>
  </svg>
  <div class="web">www.brovalt-cloud.com</div>
</section>

<!-- Envelope front -->
<section class="item envelope-front" aria-label="Envelope front">
  <div class="wordmark">BrovaLT</div>
  <div class="envelope-window"></div>
  <svg class="band" style="top:126px" width="372" height="47" viewBox="0 0 372 47">
    <polygon points="0,0 57,17 0,38" fill="var(--red)"/>
    <rect x="57" y="16" width="315" height="2.5" fill="var(--navy)"/>
    <polygon points="57,17 60,18.5 0,41 0,38" fill="var(--navy)"/>
    <polygon points="63,25 372,25 372,47 0,47 0,46" fill="var(--black)"/>
  </svg>
  <div class="web">www.brovalt-cloud.com</div>
</section>

<!-- Envelope back -->
<section class="item envelope-back" aria-label="Envelope back">
  <svg class="flap" width="370" height="172" viewBox="0 0 370 172">
    <path d="M0 0 L370 0 L352 33 Q346 43 333 45 L192 66 Q185 67 178 66 L37 45 Q24 43 18 33 Z" fill="var(--black)"/>
    <path d="M0 0 L0 172 M370 0 L370 172" stroke="#d6d6d6" stroke-width="1"/>
  </svg>
  <div class="wordmark centered">BrovaLT</div>
</section>

</body>
</html>
```